Business Card for a Creative Technology based HR services company

Our company name is Leaf8, and we build large communities of HR (human resource) and finance personnels through our mobile platform, and we conduct lots of on-line and off-line activities to get everyone constantly connected. Behind all these, we will also provide on-site HR and finance contractors to our clients, plus a host of other HR-related services. No process in our company takes more than 5-steps.
Our company slogan: Touching Your Future
Target Market(s)
All human resource (HR) and finance personnels, from new entrants to highly experienced senior professionals.
Industry/Entity Type
Finance
Colors
Designer to choose colors to be used in the design.
Look and feel
Each slider illustrates characteristics of the customer's brand and the style your logo design should communicate.

```html
<!DOCTYPE html>
<html lang="en">
<head>
<meta charset="utf-8">
<title>Leaf8 Business Card</title>
<link rel="stylesheet" href="https://fonts.googleapis.com/css2?family=Cinzel:wght@400;700&display=swap">
<style>
  :root {
    --page: #e9e9ec;
    --card: #ffffff;
    --navy: #102a4c;
    --navy-light: #1e3d66;
    --red: #d8262f;
    --ink: #3b3b3b;
  }
  * { margin: 0; padding: 0; box-sizing: border-box; }
  html, body { width: 1200px; height: 900px; overflow: hidden; background: var(--page); }
  .canvas { position: relative; width: 1200px; height: 900px; }
  .card {
    position: absolute; left: 110px; top: 170px;
    width: 980px; height: 560px;
    background: var(--card);
    border-radius: 42px;
    overflow: hidden;
    box-shadow: 0 14px 40px rgba(0,0,0,0.18);
    font-family: "Cinzel", serif;
  }
  .top-band {
    position: absolute; left: 0; top: 0;
    width: 100%; height: 150px;
    background: linear-gradient(90deg, rgba(16,42,76,0) 0%, var(--navy-light) 45%, var(--navy) 100%);
  }
  .brand-name {
    position: absolute; left: 62px; top: 190px;
    font-size: 64px; font-weight: 700; color: var(--red);
    letter-spacing: 1px; line-height: 1;
  }
  .holder { position: absolute; left: 62px; top: 290px; color: var(--red); }
  .holder-name { font-size: 36px; font-weight: 400; letter-spacing: 1px; line-height: 1.1; }
  .holder-role { font-size: 22px; margin-top: 6px; letter-spacing: 1px; }
  .contact-list {
    position: absolute; left: 552px; top: 352px;
    list-style: none; color: var(--ink);
    font-size: 17px; line-height: 1.1;
  }
  .contact-item { display: flex; align-items: flex-start; gap: 12px; margin-bottom: 6px; }
  .contact-item.plain { padding-left: 30px; margin-top: -4px; }
  .contact-icon { width: 18px; height: 18px; flex: none; margin-top: 1px; }
</style>
</head>
<body>
<main class="canvas">
  <article class="card">
    <div class="top-band" role="img" aria-label="Decorative navy band across the top of the card"></div>

    <div class="brand-name">Leaf8</div>

    <div class="holder">
      <div class="holder-name">Mark Ellison</div>
      <div class="holder-role">Owner / CEO</div>
    </div>

    <ul class="contact-list">
      <li class="contact-item">
        <svg class="contact-icon" viewBox="0 0 18 18"><circle cx="9" cy="9" r="9" fill="var(--red)"/><path d="M9 4a3 3 0 0 0-3 3c0 2.3 3 6 3 6s3-3.7 3-6a3 3 0 0 0-3-3z" fill="#fff"/></svg>
        <span>Suite # 318, Elm Bldg.</span>
      </li>
      <li class="contact-item plain"><span>NY, 40217</span></li>
      <li class="contact-item">
        <svg class="contact-icon" viewBox="0 0 18 18"><circle cx="9" cy="9" r="9" fill="var(--red)"/><path d="M6 5l2 0 1 2.5-1.2 1a6 6 0 0 0 2.7 2.7l1-1.2 2.5 1 0 2c-4 .5-8.5-4-8-8z" fill="#fff"/></svg>
        <span>212 555 0147</span>
      </li>
      <li class="contact-item">
        <svg class="contact-icon" viewBox="0 0 18 18"><circle cx="9" cy="9" r="9" fill="var(--red)"/><rect x="6" y="4" width="6" height="10" rx="1" fill="#fff"/></svg>
        <span>212 555 0193</span>
      </li>
      <li class="contact-item">
        <svg class="contact-icon" viewBox="0 0 18 18"><circle cx="9" cy="9" r="9" fill="var(--red)"/><rect x="5" y="7" width="8" height="6" fill="#fff"/><rect x="6.5" y="4" width="5" height="3" fill="#fff"/></svg>
        <span>212 555 0168</span>
      </li>
      <li class="contact-item">
        <svg class="contact-icon" viewBox="0 0 18 18"><circle cx="9" cy="9" r="9" fill="var(--red)"/><rect x="4.5" y="6" width="9" height="6.5" fill="#fff"/><path d="M4.5 6l4.5 3.5L13.5 6" fill="none" stroke="var(--red)" stroke-width="1"/></svg>
        <span>mark@leafeight.com</span>
      </li>
      <li class="contact-item">
        <svg class="contact-icon" viewBox="0 0 18 18"><circle cx="9" cy="9" r="9" fill="var(--red)"/><circle cx="9" cy="9" r="4.5" fill="none" stroke="#fff" stroke-width="1.3"/><path d="M4.5 9h9M9 4.5v9" stroke="#fff" stroke-width="1"/></svg>
        <span>www.leafeight.com</span>
      </li>
    </ul>
  </article>
</main>
</body>
</html>
```